Herausgeber suchen Design
Zielgruppe
Wir sind Herausgeber einer Festschrift für unseren Doktor-/Habilvater, Prof. Dr. Lohmeyer, und suchen ein hochwertiges Design für die Einladungskarten zu einem Symposium, im Rahmen dessen die Festschrift übergeben wird; Zielgruppe sind die Autoren der Festschrift, Alumnis und Weggefährten von Herrn Lohmeyer
Aufgabenstellung
- Maße: 210 mm x 105 mm
- Einladungskarte: geklappt; Frontseite, 2 Innenseiten, Rückseite
- Zum Text siehe Datei 'Text Einladungskarte'
- Design eher traditionell/konservativ, da es sich um einen wissenschaftlichen Hintergrund handelt (Symposium, Übergabe Festschrift)
- Die Farben sollen mit dem Cover der Festschrift korrespondieren (vgl. Datei 'Templates_Research_Vossek', dort das erste Cover (KLM_RE_T01)

```html
<!DOCTYPE html>
<html lang="de">
<head>
<meta charset="utf-8">
<title>Einladung – Symposium Festschrift</title>
<link href="https://fonts.googleapis.com/css2?family=Jost:wght@200&family=Nunito+Sans:ital,wght@0,400;0,700;1,400&display=swap" rel="stylesheet">
<style>
  :root {
    --backdrop: #e7e7e7;
    --navy: #1e3a6a;
    --accent-band: #1d7fcf;
    --panel-tint: #dce4f5;
    --name-blue: #1a7cc5;
    --ink: #111;
    --bullet: #c3d0ea;
    --divider: #cfcfcf;
    --photo-light: #9fdcf5;
    --photo-mid: #2fb4e4;
    --photo-dark: #0a5f86;
  }
  * { margin: 0; padding: 0; box-sizing: border-box; }
  html, body { width: 1200px; height: 936px; overflow: hidden; }
  body {
    background: var(--backdrop);
    position: relative;
    font-family: "Nunito Sans", sans-serif;
    color: var(--ink);
  }
  .panel { position: absolute; overflow: hidden; }

  /* Front */
  .front { left: 599px; top: 16px; width: 581px; height: 291px; background: var(--navy); }
  .front-photo {
    position: absolute; left: 0; top: 0; width: 100%; height: 127px;
    background: linear-gradient(180deg, var(--photo-dark) 0%, var(--photo-mid) 18%, var(--photo-light) 45%, var(--photo-mid) 80%, var(--photo-light) 100%);
  }
  .front-band { position: absolute; left: 0; top: 127px; width: 100%; height: 7px; background: var(--accent-band); }
  .front-title {
    position: absolute; right: 37px; top: 134px;
    font-family: "Jost", sans-serif; font-weight: 200;
    font-size: 56px; line-height: 1; letter-spacing: 1px; color: #fff;
  }

  /* Inner left */
  .inner-left { left: 18px; top: 322px; width: 581px; height: 291px; background: #fff; text-align: center; }
  .inner-left-head { position: absolute; left: 0; top: 0; width: 100%; height: 143px; background: var(--panel-tint); }
  .occasion { position: absolute; left: 0; width: 100%; top: 35px; font-size: 12px; font-weight: 700; }
  .honoree { position: absolute; left: 0; width: 100%; top: 61px; font-size: 14.5px; font-weight: 700; color: var(--name-blue); letter-spacing: .2px; }
  .venue { position: absolute; left: 0; width: 100%; top: 88px; font-size: 10px; line-height: 11.8px; }
  .editors-intro { position: absolute; left: 0; width: 100%; top: 159px; font-size: 10px; }
  .editors { position: absolute; left: 0; width: 100%; top: 182px; font-size: 10px; font-weight: 700; line-height: 11.8px; list-style: none; }
  .editors-outro { position: absolute; left: 0; width: 100%; top: 252px; font-size: 10px; }

  /* Inner right */
  .inner-right { left: 599px; top: 322px; width: 582px; height: 291px; background: #fff; border-left: 1px solid var(--divider); }
  .programme-label { position: absolute; left: 48px; top: 35px; font-size: 10px; font-style: italic; }
  .programme { position: absolute; left: 151px; top: 35px; list-style: none; font-size: 10px; line-height: 11.8px; }
  .programme li { position: relative; padding-left 0; margin-bottom: 11.7px; }
  .programme li::before {
    content: ""; position: absolute; left: -11px; top: 4px;
    width: 3.5px; height: 3.5px; border-radius: 50%; background: var(--bullet);
  }
  .programme .item-title { font-weight: 700; }
  .programme li.single { margin-bottom: 11.7px; }
  .rsvp { position: absolute; left: 158px; top: 255px; font-size: 8.8px; font-style: italic; }

  /* Back */
  .back { left: 18px; top: 629px; width: 581px; height: 290px; background: var(--navy); }
</style>
</head>
<body>

<section class="panel front">
  <div class="front-photo" role="img" aria-label="Foto eines geschlossenen Buches mit Lesebändchen in Cyan-Tönen"></div>
  <div class="front-band"></div>
  <h1 class="front-title">Einladung</h1>
</section>

<section class="panel inner-left">
  <div class="inner-left-head">
    <p class="occasion">Symposium anlässlich der Übergabe der Festschrift an</p>
    <p class="honoree">Prof. Dr. Hans-Georg Lohmeyer</p>
    <p class="venue">am 29.06.2018 um 16 Uhr<br>im Gästehaus der Universität Nordstadt,<br>Lindenallee 12, 20999 Nordstadt</p>
  </div>
  <p class="editors-intro">Die Herausgeber</p>
  <ul class="editors">
    <li>Prof. Dr. Martin Kessler</li>
    <li>Prof. Dr. Tobias Brandt</li>
    <li>Prof. Dr. Jonas R. Hartwig, StB</li>
    <li>PD Dr. Ansgar Wiebeck</li>
    <li>Dr. Lukas Ohlsen</li>
  </ul>
  <p class="editors-outro">laden herzlich ein.</p>
</section>

<section class="panel inner-right">
  <p class="programme-label">Ablauf</p>
  <ul class="programme">
    <li><span class="item-title">Begrüßung und Vorstellung der Festschrift</span><br>Prof. Dr. Martin Kessler</li>
    <li><span class="item-title">«Fortentwicklung des Corporate Governance Reportings»</span><br>Prof. Dr. Felix M. Rendel, LL.M. (London)</li>
    <li class="single"><span class="item-title">Diskussion</span></li>
    <li><span class="item-title">«Neuere Entwicklungen im Rahmen der risikoorientierten Abschlussprüfung»</span><br>Prof. Dr. Henrik D. Sander</li>
    <li class="single"><span class="item-title">Diskussion</span></li>
    <li class="single">Im Anschluss an das Symposium findet ein <span class="item-title">Umtrunk</span> statt.</li>
  </ul>
  <p class="rsvp">Um Antwort wird gebeten bis zum 18. Mai 2018 unter martina.brandes@wiso.uni-nordstadt.de</p>
</section>

<section class="panel back" aria-label="Rückseite"></section>

</body>
</html>
```